business cards and digital stationary templates for risk reduction/mitigation consulting firm
Brackenford Advisory (UK) Ltd
Tom Baverstock, MQBPFA, Tech QBWA, MSVO
Managing Director
Brackenford Advisory (UK) Ltd Ormsby Cottage Pelling Common Wexcombe SO4 7TR
tom@brackenfordadvisoryuk.co.uk
www.brackenfordadvisoruk.co.uk
I require double sided business cards and digital stationary so that I can create business letters, customer invoices and business reports all branded using microsoft word. I would also like to be able to add information to the these templates if required.

```html
<!DOCTYPE html>
<html lang="en">
<head>
<meta charset="utf-8">
<title>Brackenford Advisory – Stationery Concepts</title>
<link rel="stylesheet" href="https://fonts.googleapis.com/css2?family=Montserrat:wght@400;700&family=Open+Sans:wght@400;600&display=swap">
<style>
:root{
  --bg:#ece4d6;
  --paper:#ffffff;
  --green:#5bb031;
  --green-dark:#2f8f2a;
  --green-light:#9ed35a;
  --orange:#f08a1c;
  --ink:#555555;
  --caption:#6b5d4a;
  --faint:#eef3e8;
}
*{box-sizing:border-box;margin:0;padding:0}
html,body{width:1200px;height:598px;overflow:hidden}
body{background:var(--bg);font-family:"Open Sans",Arial,sans-serif;position:relative}
.section-title{position:absolute;left:34px;top:38px;font:400 11px "Open Sans",sans-serif;letter-spacing:2px;text-transform:uppercase;font-variant:small-caps;color:var(--caption)}
.caption{position:absolute;top:563px;font:400 10px "Open Sans",sans-serif;letter-spacing:2px;text-transform:uppercase;color:var(--caption);transform:translateX(-50%)}
.sheet{position:absolute;background:var(--paper);box-shadow:0 3px 8px rgba(0,0,0,.25);overflow:hidden}
.brand{font:700 13px "Montserrat",sans-serif;color:var(--green-dark);display:flex;align-items:center;gap:6px;line-height:1;white-space:nowrap}
.brand .dot{width:10px;height:10px;border-radius:50%;background:var(--orange);flex:none}
.wave{position:absolute;left:0;bottom:0;width:100%}
.mark-faint{position:absolute;border-radius:50%;background:var(--faint)}
.lines{position:absolute;font-size:6px;line-height:9px;color:var(--ink)}
/* cards */
.card{width:175px;height:113px;left:24px}
.card-front{top:235px}
.card-front .brand{position:absolute;left:14px;top:18px;font-size:11px}
.card-front .lines{left:14px;top:40px}
.card-back{top:367px}
.card-back .brand{position:absolute;left:50%;top:44px;transform:translateX(-50%);font-size:11px}
.card-back .lines{left:0;right:0;top:70px;text-align:center}
/* letterhead */
.letterhead{left:216px;top:29px;width:403px;height:518px}
.letterhead .brand{position:absolute;left:28px;top:24px;font-size:14px}
.letterhead .mark-faint{left:353px;top:0}
.letterhead .contact{position:absolute;left:28px;bottom:8px;font-size:6px;line-height:9px;color:#fff}
/* envelopes */
.env{width:auto}
.env-green{left:655px;top:24px;width:511px;height:204px}
.env-orange{left:689px;top:115px;width:477px;height:185px}
.env-white{left:715px;top:240px;width:451px;height:144px}
.env-white .brand{position:absolute;left:50%;top:46px;transform:translateX(-50%)}
.env-front{left:655px;top:353px;width:454px;height:170px}
.env-front .brand{position:absolute;left:22px;top:22px;font-size:12px}
.env-front .lines{left:22px;top:44px}
.env-front .mark-faint{left:300px;top:40px;width:120px;height:120px}
.flap{position:absolute;left:0;top:0;width:100%}
</style>
</head>
<body>
<div class="section-title">Stationery Concepts</div>

<div class="sheet card card-front">
  <div class="brand"><span class="dot"></span>Brackenford Advisory</div>
  <div class="lines">Tom Baverstock<br>Managing Director</div>
  <svg class="wave" viewBox="0 0 175 50" height="50" aria-hidden="true">
    <path d="M0 22 C60 2 110 36 175 12 V50 H0Z" fill="var(--orange)"/>
    <path d="M0 27 C60 8 110 40 175 18 V50 H0Z" fill="var(--paper)"/>
    <path d="M0 31 C60 14 110 44 175 24 V50 H0Z" fill="var(--green)"/>
  </svg>
</div>

<div class="sheet card card-back">
  <div class="brand"><span class="dot"></span>Brackenford Advisory</div>
  <div class="lines">www.brackenfordadvisoruk.co.uk</div>
</div>

<div class="sheet letterhead">
  <div class="brand"><span class="dot"></span>Brackenford Advisory</div>
  <div class="mark-faint" style="left:140px;top:185px;width:124px;height:124px"></div>
  <svg class="wave" viewBox="0 0 403 92" height="92" aria-hidden="true">
    <defs><linearGradient id="lhGreen" x1="0" x2="1"><stop offset="0" stop-color="var(--green-dark)"/><stop offset="1" stop-color="var(--green-light)"/></linearGradient></defs>
    <path d="M0 30 C120 10 250 48 403 8 V92 H0Z" fill="var(--orange)"/>
    <path d="M0 36 C120 16 250 54 403 14 V92 H0Z" fill="var(--paper)"/>
    <path d="M0 41 C120 22 250 60 403 20 V92 H0Z" fill="url(#lhGreen)"/>
  </svg>
  <div class="contact">Tel 01632 960418<br>tom@brackenfordadvisoryuk.co.uk<br>www.brackenfordadvisoruk.co.uk<br>Ormsby Cottage Pelling Common Wexcombe SO4 7TR</div>
</div>
<div class="caption" style="left:418px">Letter Head Option 1</div>

<div class="sheet env-green">
  <svg class="flap" viewBox="0 0 511 84" height="84" preserveAspectRatio="none" aria-hidden="true">
    <defs><linearGradient id="flapGreen" x1="0" x2="1"><stop offset="0" stop-color="var(--green-light)"/><stop offset="1" stop-color="var(--green-dark)"/></linearGradient></defs>
    <path d="M0 0 H511 V60 Q255 90 0 60Z" fill="url(#flapGreen)"/>
  </svg>
</div>
<div class="sheet env-orange">
  <svg class="flap" viewBox="0 0 477 66" height="66" preserveAspectRatio="none" aria-hidden="true">
    <path d="M0 0 H477 V48 Q238 72 0 48Z" fill="var(--orange)"/>
  </svg>
</div>
<div class="sheet env-white">
  <div class="brand"><span class="dot"></span>Brackenford Advisory</div>
</div>
<div class="sheet env-front">
  <div class="brand"><span class="dot"></span>Brackenford Advisory</div>
  <div class="lines">Ormsby Cottage<br>Pelling Common<br>Wexcombe SO4 7TR</div>
  <div class="mark-faint"></div>
</div>
<div class="caption" style="left:912px">Envelope Option 2</div>
</body>
</html>
```